Domain Name Contest

We need some help choosing a domain name for a Startup web development company.
Services offers: All comprehensive web/mobile application design and development.
Customers: Global

Rules for the Domain Name :
1) Domain name suggestion should be available for registration (cross check with brightwren before suggesting)
2) Should be highly creative and easy to spell
3) Domain name should be smaller
4) Should be of universal name(.com preferred)

```html
<!DOCTYPE html>
<html lang="en">
<head>
<meta charset="UTF-8">
<title>Domain Available – quillappworks.com</title>
<link rel="stylesheet" href="https://fonts.googleapis.com/css2?family=Poppins:wght@600;700&display=swap">
<style>
  :root {
    --ink: #1b1b1b;
    --paper: #ffffff;
    --brand-green: #00843d;
    --card-edge: #dcdcdc;
  }
  html, body {
    margin: 0;
    padding: 0;
    overflow: hidden;
    background: var(--paper);
  }
  .canvas {
    position: relative;
    width: 1200px;
    height: 509px;
    overflow: hidden;
    background: var(--paper);
    color: var(--ink);
    font-family: "Poppins", sans-serif;
  }
  .headline {
    position: absolute;
    left: 0;
    top: 4px;
    margin: 0;
    font-size: 73px;
    font-weight: 700;
    letter-spacing: -1px;
    line-height: 1;
    text-transform: uppercase;
    white-space: nowrap;
  }
  .subline {
    position: absolute;
    left: 0;
    top: 76px;
    margin: 0;
    font-size: 46px;
    font-weight: 700;
    letter-spacing: -0.5px;
    line-height: 1;
    text-transform: uppercase;
    white-space: nowrap;
  }
  .result-card {
    position: absolute;
    left: 8px;
    top: 202px;
    width: 1192px;
    height: 330px;
    border-top: 19px solid var(--brand-green);
    border-left: 3px solid var(--card-edge);
    box-sizing: border-box;
    background: var(--paper);
  }
  .domain-name {
    position: absolute;
    left: 58px;
    top: 44px;
    margin: 0;
    font-size: 64px;
    font-weight: 600;
    line-height: 1;
    letter-spacing: -0.5px;
    white-space: nowrap;
  }
  .domain-tld {
    position: absolute;
    left: 56px;
    top: 126px;
    margin: 0;
    font-size: 139px;
    font-weight: 600;
    line-height: 1;
    letter-spacing: -1px;
    white-space: nowrap;
  }
</style>
</head>
<body>
  <main class="canvas">
    <h1 class="headline">Yes! Your domain is available.</h1>
    <p class="subline">Buy it before someone else does.</p>
    <section class="result-card">
      <p class="domain-name">quillappworks</p>
      <p class="domain-tld">.com</p>
    </section>
  </main>
</body>
</html>
```